business card - Helicopter Flight Services, Flight School, etc.

We need a business card design for a new helicopter service.

We offer Helicopter Flight Services, Aerial Filming & Photography, Flight School, and Helicopter Tours. In that order.

Summit BladeLine, Inc.
Harold Tebbets
SummitBladeline@Mailvane.com
555-014-2786

Based at the Corvell Airport in Van Nuys, CA. The final design should communicate integrity and safety. Pictures or logos at your discretion.

Card back side - surprise me.

```html
<!DOCTYPE html>
<html lang="en">
<head>
<meta charset="utf-8">
<title>Summit BladeLine, Inc. — Business Card</title>
<link rel="stylesheet" href="https://fonts.googleapis.com/css2?family=Libre+Baskerville:wght@700&family=Arimo:wght@400&display=swap">
<style>
  :root {
    --bg: #e9e6e1;
    --card-white: #ffffff;
    --brand-blue: #1f5c9e;
    --brand-blue-deep: #18508c;
    --ink: #111111;
    --text-light: #ffffff;
    --sky-top: #dfe6ee;
    --sky-bottom: #c9d3de;
  }
  * { margin: 0; padding: 0; box-sizing: border-box; }
  html, body { width: 1200px; height: 902px; overflow: hidden; }
  body {
    background: var(--bg);
    font-family: "Arimo", Arial, sans-serif;
    display: flex;
    align-items: center;
    justify-content: center;
    gap: 40px;
  }
  .card {
    position: relative;
    width: 540px;
    height: 308px;
    overflow: hidden;
    background: var(--card-white);
    box-shadow: 0 2px 8px rgba(0,0,0,.18);
  }
  .card__shape { position: absolute; inset: 0; }
  .brand {
    position: absolute;
    text-align: center;
    line-height: 1;
  }
  .brand__name {
    font-family: "Libre Baskerville", Georgia, serif;
    font-weight: 700;
    font-size: 31px;
    letter-spacing: -0.5px;
  }
  .brand__services {
    font-size: 19px;
    margin-top: 6px;
    color: var(--ink);
  }
  .card--front .brand { top: 42px; left: 70px; right: 20px; }
  .card--front .brand__name { color: var(--brand-blue); }
  .card--back .brand { top: 112px; left: 0; right: 0; }
  .card--back .brand__name { color: var(--ink); }

  .holder {
    position: absolute;
    left: 28px;
    bottom: 28px;
    color: var(--text-light);
    font-size: 20px;
  }
  .contact {
    position: absolute;
    left: 190px;
    top: 212px;
    padding-left: 10px;
    border-left: 1.5px solid var(--text-light);
    list-style: none;
    color: var(--text-light);
    font-size: 11.5px;
  }
  .contact__item {
    display: flex;
    align-items: center;
    gap: 6px;
    height: 19px;
  }
  .contact__icon { width: 12px; height: 12px; flex: none; }
  .card__photo { position: absolute; inset: 0; background: linear-gradient(180deg, var(--sky-top), var(--sky-bottom)); }
</style>
</head>
<body>

  <section class="card card--front">
    <svg class="card__shape" viewBox="0 0 540 308" aria-hidden="true">
      <path d="M0 205 C150 235 430 205 540 40 L540 308 L0 308 Z" fill="var(--brand-blue)"/>
      <path d="M40 212 C190 232 420 200 510 72 C440 190 200 226 40 212 Z" fill="var(--ink)"/>
    </svg>
    <div class="brand">
      <div class="brand__name">Summit BladeLine, Inc.</div>
      <div class="brand__services">Airport · Tour guide · Heliport</div>
    </div>
    <div class="holder">Harold Tebbets</div>
    <ul class="contact">
      <li class="contact__item">
        <svg class="contact__icon" viewBox="0 0 12 12"><rect width="12" height="12" fill="#fff"/><path d="M3 3h2l.6 1.6-1 .7a5 5 0 0 0 2.1 2.1l.7-1L9 7v2c-3.5 0-6-2.5-6-6z" fill="var(--brand-blue)"/></svg>
        555-014-2786
      </li>
      <li class="contact__item">
        <svg class="contact__icon" viewBox="0 0 12 12"><rect width="12" height="12" fill="#fff"/></svg>
        Summit BladeLine Inc.
      </li>
      <li class="contact__item">
        <svg class="contact__icon" viewBox="0 0 12 12"><rect width="12" height="12" fill="#fff"/><rect x="2" y="3.5" width="8" height="5" fill="none" stroke="var(--brand-blue)"/><path d="M2 3.5l4 3 4-3" fill="none" stroke="var(--brand-blue)"/></svg>
        SummitBladeline@Mailvane.com
      </li>
      <li class="contact__item">
        <svg class="contact__icon" viewBox="0 0 12 12"><rect width="12" height="12" fill="#fff"/><path d="M6 10.5 3.3 6.2a3 3 0 1 1 5.4 0z" fill="var(--brand-blue)"/><circle cx="6" cy="4.6" r="1" fill="#fff"/></svg>
        4870 Larkspur Ave. Ste.B Corvell, CA 91406
      </li>
    </ul>
  </section>

  <section class="card card--back">
    <div class="card__photo" role="img" aria-label="Faded photograph of a helicopter flying above a coastal city under a pale sky"></div>
    <div class="brand">
      <div class="brand__name">Summit BladeLine, Inc.</div>
      <div class="brand__services">Airport · Tour guide · Heliport</div>
    </div>
  </section>

</body>
</html>
```